Bamboo Toothbrush packaging design

We need a packaging design for a pack of 4 bamboo toothbrushes. The front of the package would need to include the company logo, name of the product - Bamboo Toothbrush, 100% plastic free, and 10% of profit will go to environmental charities . Would like to see some simple or creative graphics to send the message.

Target Market(s)

Retail

Font styles to use
Sans Serif

Colors

Designer to choose colors to be used in the design.

Requirements
Must have
• Just be creative.

```html
<!DOCTYPE html>
<html lang="en">
<head>
<meta charset="utf-8">
<title>Reed Finch Bamboo Toothbrush – Carton Panels</title>
<link href="https://fonts.googleapis.com/css2?family=Montserrat:wght@500;600;700;800&family=Open+Sans:wght@400;600&display=swap" rel="stylesheet">
<style>
  :root{
    --bg:#e4e5e3;
    --kraft:#c9ab80;
    --kraft-dark:#b8996d;
    --ink:#1c2d38;
    --ink-soft:#3a4a55;
    --paper:#ffffff;
    --leaf:#5c9a3a;
    --fold:#a88b60;
  }
  *{box-sizing:border-box;margin:0;padding:0}
  html,body{width:1200px;height:1200px;overflow:hidden;background:var(--bg)}
  body{font-family:"Montserrat",sans-serif;color:var(--ink)}
  .carton{position:absolute;left:140px;top:80px;width:920px;height:1040px;display:flex;box-shadow:0 6px 24px rgba(0,0,0,.12)}
  .panel{position:relative;height:100%;background:var(--kraft);border-right:1px dashed var(--fold)}
  .panel:last-child{border-right:none}
  .panel--front{width:260px}
  .panel--side{width:200px}
  .panel--back{width:260px}

  .brand-band{position:absolute;left:30px;top:40px;width:200px;height:72px;background:var(--ink);display:flex;align-items:center;justify-content:center}
  .brand-name{color:var(--paper);font-weight:600;font-size:22px;font-family:"Montserrat",sans-serif}
  .product-title{position:absolute;left:30px;top:140px;width:200px}
  .product-title .line1{font-weight:800;font-size:40px;letter-spacing:.5px;line-height:1}
  .product-title .line2{font-weight:700;font-size:22px;line-height:1.2;border-bottom:1.5px solid var(--ink);padding-bottom:6px}
  .product-title .tagline{font-weight:600;font-size:13px;margin-top:6px}
  .pack{position:absolute;left:30px;top:262px;display:flex;align-items:center;gap:6px;font-weight:800;font-size:28px}
  .pack .count{width:46px;height:46px;border-radius:50%;background:var(--ink);color:var(--paper);display:flex;align-items:center;justify-content:center;font-size:28px}
  .brush-art{position:absolute;left:95px;top:340px;width:70px;height:470px;border-radius:30px;background:linear-gradient(180deg,#2a2a2a 0 28%,rgba(28,45,56,.12) 28% 100%)}
  .claims{position:absolute;left:22px;top:830px;width:220px}
  .claim-plastic{display:flex;align-items:flex-start;gap:4px}
  .claim-plastic .big{font-weight:800;font-size:28px;line-height:1}
  .claim-plastic .small{font-weight:700;font-size:12px;line-height:1.1}
  .claim-charity{margin-top:12px;display:flex;align-items:flex-start;gap:4px}
  .claim-charity .big{font-weight:800;font-size:28px;line-height:1}
  .claim-charity .small{font-weight:700;font-size:12px;line-height:1.1;padding-top:2px}
  .claim-charity-sub{font-weight:700;font-size:12px;margin-top:2px}
  .charity-art{position:absolute;left:110px;top:928px;width:40px;height:34px;border-radius:50%;background:radial-gradient(circle,#8cc466,var(--leaf))}
  .certs{position:absolute;left:30px;bottom:22px;display:flex;gap:14px}
  .cert{width:34px;height:34px;border:2px solid var(--ink);border-radius:4px}
  .cert--round{border-radius:50%}

  .side-copy{position:absolute;left:110px;top:40px;height:260px;writing-mode:vertical-rl;font-family:"Open Sans",sans-serif;font-size:10.5px;line-height:1.35;color:var(--ink-soft)}
  .contacts{position:absolute;left:40px;top:530px;height:330px;writing-mode:vertical-rl;display:flex;flex-direction:column;gap:10px;font-family:"Montserrat",sans-serif;font-weight:500;font-size:19px}
  .contact{display:flex;align-items:center;gap:10px}
  .contact .dot{width:20px;height:20px;border-radius:50%;background:var(--ink);display:inline-block}
  .marks{position:absolute;left:40px;top:880px;display:flex;flex-direction:column;gap:8px}
  .mark{width:22px;height:22px;border:2px solid var(--ink);border-radius:4px}
  .mark--round{border-radius:50%}

  .back-band{position:absolute;left:0;top:0;width:100%;height:60px;background:var(--ink)}
  .back-copy{position:absolute;left:30px;top:120px;width:200px;text-align:center;font-family:"Open Sans",sans-serif;font-size:11px;line-height:1.4;color:var(--ink-soft)}
  .bamboo-art{position:absolute;left:60px;top:390px;width:140px;height:330px;background:linear-gradient(160deg,#4a4a4a,#2f2f2f);border-radius:6px;opacity:.85}
  .recycle{position:absolute;left:0;width:100%;top:770px;text-align:center}
  .recycle svg{display:block;margin:0 auto 8px}
  .recycle-label{font-family:"Open Sans",sans-serif;font-size:11px;line-height:1.3;letter-spacing:.4px}
  .address{position:absolute;left:0;width:100%;top:900px;text-align:center;font-family:"Open Sans",sans-serif;font-size:12px;line-height:1.35}
  .made-in{position:absolute;left:0;width:100%;top:985px;text-align:center;font-weight:600;font-size:15px}

  .features{position:absolute;left:40px;top:50px;display:flex;flex-direction:column;gap:50px}
  .feature{position:relative;width:120px;height:190px}
  .feature svg{position:absolute;left:0;top:0}
  .feature-label{position:absolute;left:38px;top:28px;height:170px;border:1.5px solid var(--ink);writing-mode:vertical-rl;font-weight:500;font-size:14px;letter-spacing:.5px;line-height:1.15;padding:8px 5px;text-align:center;display:flex;justify-content:center}
</style>
</head>
<body>
<main class="carton">

  <section class="panel panel--front" aria-label="Front panel">
    <div class="brand-band"><span class="brand-name">Reed Finch</span></div>
    <div class="product-title">
      <div class="line1">BAMBOO</div>
      <div class="line2">TOOTHBRUSH</div>
      <div class="tagline">Sustainable Oral Care</div>
    </div>
    <div class="pack"><span class="count">4</span>PACK</div>
    <div class="brush-art" role="img" aria-label="Line illustration of a bamboo toothbrush with charcoal bristles"></div>
    <div class="claims">
      <div class="claim-plastic"><span class="big">100%</span><span class="small">PLASTIC<br>FREE</span></div>
      <div class="claim-charity"><span class="big">10%</span><span class="small">of Profit<br>Will Go To</span></div>
      <div class="claim-charity-sub">Environmental Charities</div>
    </div>
    <div class="charity-art" role="img" aria-label="Illustration of a hand holding the green earth"></div>
    <div class="certs"><span class="cert"></span><span class="cert"></span><span class="cert cert--round"></span></div>
  </section>

  <section class="panel panel--side" aria-label="Contact side panel">
    <p class="side-copy">Each brush has a bamboo handle and soft charcoal bristles. Replace every three months, then compost the handle at home. Store dry between uses. Keep away from heat.</p>
    <div class="contacts">
      <div class="contact"><span class="dot"></span>/reedfinch</div>
      <div class="contact"><span class="dot"></span>hello@reedfinch.com</div>
      <div class="contact"><span class="dot"></span>www.reedfinch.com</div>
    </div>
    <div class="marks"><span class="mark"></span><span class="mark"></span><span class="mark mark--round"></span></div>
  </section>

  <section class="panel panel--back" aria-label="Back panel">
    <div class="back-band"></div>
    <p class="back-copy">Each brush has a bamboo handle and soft charcoal bristles. Replace every three months, then compost the handle at home. Store dry between uses. Keep away from heat.</p>
    <div class="bamboo-art" role="img" aria-label="Illustration of bamboo stalks with leaves"></div>
    <div class="recycle">
      <svg width="56" height="56" viewBox="0 0 56 56" aria-hidden="true"><circle cx="28" cy="28" r="24" fill="none" stroke="var(--ink)" stroke-width="4"/></svg>
      <div class="recycle-label">Recycled<br>Cardboard Box</div>
    </div>
    <div class="address">address :<br>XXXXXXXXXXXX<br>XXXXXXXXXXXX<br>XXXXXXXXXXXXX</div>
    <div class="made-in">MADE IN XXXXXX</div>
  </section>

  <section class="panel panel--side" aria-label="Features side panel">
    <div class="features">
      <div class="feature">
        <svg width="40" height="40" viewBox="0 0 40 40" aria-hidden="true"><path d="M4 20 L14 34 L36 4" fill="none" stroke="var(--ink)" stroke-width="3"/></svg>
        <div class="feature-label">NATURALLY<br>ANTIBACTERIAL</div>
      </div>
      <div class="feature">
        <svg width="40" height="40" viewBox="0 0 40 40" aria-hidden="true"><path d="M4 20 L14 34 L36 4" fill="none" stroke="var(--ink)" stroke-width="3"/></svg>
        <div class="feature-label">NO<br>CHEMICALS</div>
      </div>
      <div class="feature">
        <svg width="40" height="40" viewBox="0 0 40 40" aria-hidden="true"><path d="M4 20 L14 34 L36 4" fill="none" stroke="var(--ink)" stroke-width="3"/></svg>
        <div class="feature-label">COMPOSTABLE<br>HANDLE</div>
      </div>
      <div class="feature">
        <svg width="40" height="40" viewBox="0 0 40 40" aria-hidden="true"><path d="M4 20 L14 34 L36 4" fill="none" stroke="var(--ink)" stroke-width="3"/></svg>
        <div class="feature-label">ERGONOMIC<br>DESIGN</div>
      </div>
    </div>
  </section>

</main>
</body>
</html>
```